Flyer Design Project for our Parenting Psychologists at the Bright Harbour Wellbeing Clinic

At the Bright Harbour Wellbeing Clinic we have expert Parenting Psychologists.

Parenting Psychologists provide practical, step by step assistance to parents who are struggling with their children's behavioural and emotional problems.

We need a DL size brochure that will be appealing to parents. The brochure will be on show in schools, kindergartens and GP clinics.

In terms of style it will be in line with our website and stationery that I will attach.

www.brightharbourwellbeing.com.au
Updates

Hi Everyone,
Thanks for putting forward your proposals, there are a couple there that I am very interested in. I am looking to see if there is a way that I can change my brief to guaranteed as I am definitely going to be using one of the designs for sure.
I have emailed ArtFolkly and as soon as I get an answer I will change it if I can.
If anyone out there already knows the answer please let me know :-)
Thanks,
Marnie.

Hi Again,

I worked it out myself!!

I have now changed this to a committed project.

Kind regards,
Marnie.

Reason: I have 46 designs now and need more time to work out which is best!

Target Market(s)

The target will be educated professional parents motivated to get professional help. And doctors and teachers who will pass on the brochures 2 parents

Industry/Entity Type

Health

Requirements
Must have
• I want one DL size brochure. Back and front.

We need text (below) and our contact details. Our logo.

9362 4158
Level 2, 2071 Pellbrook Rd, Ferndale Heights 3264

Text:
Parents want the best for their kids. They want kids that are happy, healthy and well behaved.

So why is it so hard? Parents of toddlers, primary schoolers and teenagers alike say that they are frustrated by constant nagging, bribing and yelling, they don't know what to try next. Some parents worry that their children are unhappy. Struggling at school, not making friends or coping with bigger problems.

The good news is that getting your children to behave more co-operatively doesn't need to be difficult or mysterious. We all know that kids don't come with manuals, but there are skills every parent can learn to make parenting easier. In a few sessions with a Parenting Psychologist, you will receive step by step guidance in how to talk to your children in a way that will be much more effective getting them to behave in a respectful and co-operative way around the home and in public. You will learn how to help your child cope with problems they are going through. They can help you reconnect with your kids so you can enjoy being a parent again.

Nice to have
• Themes consistent with our website
and letterhead, business cards. I will attach these.
Should not have
• I don't want it to look too cluttered so if the text I have provided up above looks too crowded then I will edit it.

```html
<!DOCTYPE html>
<html lang="en">
<head>
<meta charset="utf-8">
<title>Bright Harbour Wellbeing Clinic – Parenting DL Flyer</title>
<link href="https://fonts.googleapis.com/css2?family=Arimo:wght@400;700&family=Roboto:wght@300;400;700&family=Tinos&display=swap" rel="stylesheet">
<style>
  :root {
    --stage: #000000;
    --paper: #ffffff;
    --green-light: #52f592;
    --green-mid: #3fe597;
    --green-soft: #47ee95;
    --green-deep: #1a8a3e;
    --brand-green: #1f8a3d;
    --brand-grey: #8d9c98;
    --ink: #1b1b1b;
    --band-1: #6ab9bf;
    --band-2: #86f2c9;
    --band-3: #6fcbb0;
    --band-4: #72999c;
    --band-5: #86f2c9;
    --label: #ffffff;
  }
  * { box-sizing: border-box; margin: 0; padding: 0; }
  html, body {
    width: 1200px; height: 1200px; overflow: hidden;
    background: var(--stage);
  }
  .stage { position: relative; width: 1200px; height: 1200px; }
  .panel {
    position: absolute; width: 425px; height: 900px;
    background: var(--paper); overflow: hidden;
    font-family: "Roboto", Arial, sans-serif;
  }
  .panel--front { left: 135px; top: 129px; }
  .panel--back { left: 658px; top: 130px; }
  .panel__art { position: absolute; inset: 0; width: 425px; height: 900px; }

  .headline {
    position: absolute; left: 45px; top: 48px; width: 335px;
    color: var(--paper); font-weight: 300; font-size: 29px; line-height: 33.5px;
  }
  .headline strong { font-weight: 700; }

  .body-copy {
    position: absolute; left: 45px; top: 54px; width: 352px;
    color: var(--paper); font-family: "Arimo", Arial, sans-serif;
    font-weight: 400; font-size: 15px; line-height: 21.1px;
    hyphens: auto; -webkit-hyphens: auto;
  }
  .body-copy p + p { margin-top: 21px; }

  .brand { position: absolute; display: flex; align-items: center; }
  .brand--front { left: 127px; top: 755px; gap: 22px; }
  .brand--back { left: 111px; top: 677px; gap: 24px; }
  .brand__dot { border-radius: 50%; background: var(--brand-green); flex: none; }
  .brand--front .brand__dot { width: 81px; height: 81px; }
  .brand--back .brand__dot { width: 62px; height: 62px; }
  .brand__name {
    color: var(--brand-grey); font-weight: 400; text-transform: uppercase;
  }
  .brand--front .brand__name { font-size: 16px; line-height: 21px; letter-spacing: 2.4px; }
  .brand--back .brand__name { font-size: 14px; line-height: 18px; letter-spacing: 2.6px; }

  .contact {
    position: absolute; left: 0; width: 425px; text-align: center;
    font-family: "Arimo", Arial, sans-serif;
  }
  .contact__address { top: 762px; font-size: 15px; color: var(--ink); }
  .contact__web { top: 788px; font-size: 15px; font-weight: 700; color: var(--brand-green); }
  .contact__call {
    top: 822px; display: flex; justify-content: center; align-items: center;
    color: var(--brand-green);
  }
  .contact__call-label { font-weight: 400; font-size: 26px; padding-right: 8px; border-right: 1px solid var(--brand-green); line-height: 36px; }
  .contact__call-number { font-weight: 700; font-size: 33px; padding-left: 8px; }

  .bands { position: absolute; left: 0; bottom: 0; width: 425px; height: 29px; display: flex; }
  .bands span { flex: 1; }
  .bands span:nth-child(1) { background: var(--band-1); }
  .bands span:nth-child(2) { background: var(--band-2); }
  .bands span:nth-child(3) { background: var(--band-3); }
  .bands span:nth-child(4) { background: var(--band-4); }
  .bands span:nth-child(5) { background: var(--band-5); }

  .side-label {
    position: absolute; color: var(--label);
    font-family: "Tinos", "Times New Roman", serif; font-size: 44px;
    width: 200px; text-align: center;
  }
  .side-label--front { left: 189px; top: 1074px; }
  .side-label--back { left: 782px; top: 1064px; }
</style>
</head>
<body>
<main class="stage">

  <section class="panel panel--front">
    <svg class="panel__art" viewBox="0 0 425 900">
      <defs>
        <linearGradient id="photoTone" x1="0" y1="0" x2="1" y2="1">
          <stop offset="0" stop-color="#8a9a6a"/>
          <stop offset="0.3" stop-color="#7c98b8"/>
          <stop offset="0.6" stop-color="#c48a7a"/>
          <stop offset="1" stop-color="#79b24a"/>
        </linearGradient>
        <linearGradient id="greyFade" x1="0" y1="0" x2="1" y2="0">
          <stop offset="0" stop-color="#ffffff"/>
          <stop offset="1" stop-color="#cfcfcf"/>
        </linearGradient>
      </defs>
      <path d="M0 0 H425 V254 Q210 252 0 180 Z" fill="var(--green-mid)"/>
      <path d="M140 0 Q300 90 425 120 V0 Z" fill="var(--green-light)" opacity="0.6"/>
      <path d="M0 40 Q180 20 425 210 V254 Q210 252 0 180 Z" fill="var(--green-soft)" opacity="0.5"/>
      <path d="M0 184 Q210 256 425 258 V534 Q270 650 0 671 Z" fill="url(#photoTone)" role="img" aria-label="Photo of a smiling mother crouching on grass with her toddler in denim overalls"/>
      <path d="M0 671 Q270 650 425 534 V600 Q380 670 250 700 Q120 720 0 697 Z" fill="var(--green-deep)"/>
      <path d="M425 534 Q330 610 200 650" fill="none" stroke="#ffffff" stroke-width="3"/>
      <path d="M250 700 Q360 680 425 600 V800 Q360 720 250 700 Z" fill="url(#greyFade)"/>
    </svg>
    <h1 class="headline"><strong>Parents</strong> want the best for their <strong>kids</strong>. They want kids that are <strong>happy, healthy</strong> and <strong>well behaved</strong>.</h1>
    <div class="brand brand--front">
      <span class="brand__dot"></span>
      <span class="brand__name">Bright Harbour<br>Wellbeing<br>Clinic</span>
    </div>
    <div class="bands"><span></span><span></span><span></span><span></span><span></span></div>
  </section>

  <section class="panel panel--back">
    <svg class="panel__art" viewBox="0 0 425 900" aria-hidden="true">
      <path d="M0 0 H425 V516 Q260 600 0 587 Z" fill="var(--green-light)"/>
      <path d="M0 0 H425 V90 Q200 40 0 120 Z" fill="var(--green-mid)" opacity="0.7"/>
      <path d="M0 250 Q220 180 425 320 V516 Q300 420 0 470 Z" fill="var(--green-mid)" opacity="0.45"/>
    </svg>
    <div class="body-copy">
      <p>So why is it so hard? Parents of toddlers, primary schoolers and teenagers alike say that they are frustrated by constant nagging, bribing and yelling, they don’t know what to try next. Some parents worry that their children are unhappy. Struggling at school, not making friends or coping with bigger problems.</p>
      <p>The good news is that getting your children to behave more co-operatively doesn’t need to be difficult or mysterious. We all know that kids don’t come with manuals, but there are skills every parent can learn to make parenting easier. In a few sessions with a Parenting Psychologist, you will receive step by step guidance in how to talk to your children in a way that will be much more effective getting them to behave in a respectful and co-operative way around the home and in public. You will learn how to help your child cope with problems they are going through. They can help you reconnect with your kids so you can enjoy being a parent again.</p>
    </div>
    <div class="brand brand--back">
      <span class="brand__dot"></span>
      <span class="brand__name">Bright Harbour<br>Wellbeing<br>Clinic</span>
    </div>
    <p class="contact contact__address">Level 2, 2071 Pellbrook Rd, Ferndale Heights 3264</p>
    <p class="contact contact__web">www.brightharbourwellbeing.com.au</p>
    <p class="contact contact__call"><span class="contact__call-label">CALL NOW</span><span class="contact__call-number">9362 4158</span></p>
    <div class="bands"><span></span><span></span><span></span><span></span><span></span></div>
  </section>

  <p class="side-label side-label--front">Front</p>
  <p class="side-label side-label--back">Back</p>
</main>
</body>
</html>
```